Oven Cleaning flyer design

Hi there,
I need help designing a letterbox flyer. It needs to be DL size.
I have attached a rough design made with Chat GPT.
Would like back and front, have my business colors.
Please find attached mock up of what I would roughly like.
Also find attached logo.
Thank you

Target Market(s)

Home owners over 40

Industry/Entity Type

Cleaning

Requirements
Must have
• Logo, before after of oven, brand colors

```html
<!DOCTYPE html>
<html lang="en">
<head>
<meta charset="utf-8">
<title>Gleamworks Ovens – DL Flyer</title>
<link rel="stylesheet" href="https://fonts.googleapis.com/css2?family=Red+Hat+Display:wght@400;500;600;700;800&family=Anton&display=swap">
<style>
  :root {
    --teal: #4fc3cf;
    --teal-deep: #3bb3c0;
    --ink: #1d1d1f;
    --charcoal: #2b2e33;
    --white: #ffffff;
    --stage: #e4e4e4;
    --photo-dirty-a: #8a6a3e;
    --photo-dirty-b: #b9b4ad;
    --photo-clean-a: #c9ccd0;
    --photo-clean-b: #8e9398;
  }
  * { box-sizing: border-box; margin: 0; padding: 0; }
  html, body { width: 944px; height: 1200px; overflow: hidden; }
  body {
    background: var(--stage);
    font-family: "Red Hat Display", Arial, sans-serif;
    color: var(--ink);
    position: relative;
  }
  .flyer {
    position: absolute;
    top: 185px;
    width: 400px;
    height: 848px;
    background: var(--white);
    overflow: hidden;
    text-align: center;
  }
  .flyer--front { left: 61px; }
  .flyer--back { left: 497px; }

  .brand {
    position: absolute;
    display: flex;
    align-items: center;
    gap: 14px;
  }
  .brand__dot {
    width: 62px; height: 62px;
    border-radius: 50%;
    background: var(--teal);
    flex: none;
  }
  .brand__name {
    font-weight: 800;
    font-size: 27px;
    line-height: 1.05;
    letter-spacing: 2px;
    text-transform: uppercase;
    color: var(--ink);
    text-align: left;
  }
  .flyer--front .brand { left: 44px; top: 48px; }
  .flyer--back .brand { left: 52px; top: 726px; }

  .front__headline {
    position: absolute; left: 0; right: 0; top: 188px;
    font-size: 34px; font-weight: 600; line-height: 43px;
    color: var(--teal);
  }
  .front__intro {
    position: absolute; left: 40px; right: 40px; top: 292px;
    font-size: 13.5px; line-height: 17.5px;
  }
  .front__band {
    position: absolute; left: 0; right: 0; top: 590px; bottom: 0;
    background: var(--charcoal);
  }
  .proof {
    position: absolute; left: 49px; top: 365px;
    width: 302px; height: 302px;
    background: var(--teal);
  }
  .proof__frame {
    position: absolute; left: 10px; top: 20px;
    width: 282px; height: 242px;
    background: var(--white);
  }
  .proof__photo {
    position: absolute; top: 10px;
    width: 128px; height: 220px;
  }
  .proof__photo--before { left: 10px; background: linear-gradient(180deg, var(--photo-dirty-b) 0%, #6d6a66 45%, var(--photo-dirty-a) 100%); }
  .proof__photo--after { left: 142px; background: linear-gradient(180deg, var(--photo-clean-a) 0%, var(--photo-clean-b) 60%, #d9dcdf 100%); }
  .proof__label {
    position: absolute; top: 265px;
    font-family: "Anton", Impact, sans-serif;
    font-style: italic;
    font-size: 15px;
    color: var(--ink);
    letter-spacing: 0.5px;
  }
  .proof__label--before { left: 62px; }
  .proof__label--after { left: 195px; }

  .front__cta {
    position: absolute; left: 0; right: 0; top: 697px;
    font-size: 13.5px; line-height: 18px; color: var(--white);
  }
  .front__phone {
    position: absolute; left: 0; right: 0; top: 750px;
    font-size: 22px; font-weight: 700; color: var(--teal);
  }
  .front__web {
    position: absolute; left: 0; right: 0; top: 798px;
    font-size: 13.5px; letter-spacing: 2.4px; color: var(--white);
  }

  .back__wave { position: absolute; left: 0; top: 0; width: 400px; height: 360px; }
  .back__headline {
    position: absolute; left: 0; right: 0; top: 44px;
    font-size: 32px; font-weight: 700; line-height: 43px; color: var(--white);
  }
  .back__about {
    position: absolute; left: 36px; right: 36px; top: 150px;
    font-size: 12.6px; line-height: 17.3px; color: var(--white);
  }
  .offer {
    position: absolute; left: 0; right: 0; top: 380px;
    font-size: 25px; font-weight: 400; line-height: 33px;
  }
  .offer__amount { color: var(--teal); font-weight: 700; }
  .promises {
    position: absolute; left: 0; right: 0; top: 472px;
    list-style: none; font-size: 15px; line-height: 20.5px;
  }
  .contact-box {
    position: absolute; left: 55px; top: 558px;
    width: 289px; height: 83px;
    background: #000;
    padding-top: 12px;
  }
  .contact-box__phone { font-size: 22px; font-weight: 700; color: var(--teal); line-height: 28px; }
  .contact-box__web { font-size: 19px; color: var(--white); line-height: 26px; }
  .extras {
    position: absolute; left: 0; right: 0; top: 663px;
    font-size: 13px; font-weight: 500;
  }
</style>
</head>
<body>

<section class="flyer flyer--front">
  <div class="brand">
    <span class="brand__dot"></span>
    <span class="brand__name">Gleamworks<br>Ovens</span>
  </div>

  <h1 class="front__headline">Bring Your Oven<br>Back to Life</h1>
  <p class="front__intro">Professional, non-caustic oven cleaning that removes built-up grease, smoke, and burnt grime - leaving your oven looking fresh again.</p>

  <div class="front__band"></div>

  <figure class="proof">
    <div class="proof__frame">
      <div class="proof__photo proof__photo--before" role="img" aria-label="Photo of a dirty oven interior with burnt grease on the open door"></div>
      <div class="proof__photo proof__photo--after" role="img" aria-label="Photo of the same oven interior after cleaning, glass door spotless"></div>
    </div>
    <span class="proof__label proof__label--before">BEFORE</span>
    <span class="proof__label proof__label--after">AFTER</span>
  </figure>

  <p class="front__cta">Call Now for<br>Fast, Professional Service</p>
  <p class="front__phone">0400 528 193</p>
  <p class="front__web">gleamworksovens.com.au</p>
</section>

<section class="flyer flyer--back">
  <svg class="back__wave" viewBox="0 0 400 360" aria-hidden="true">
    <path d="M0 0 H400 V292 C330 310 260 345 190 352 C120 358 60 330 0 318 Z" fill="#000"/>
    <path d="M0 0 H400 V296 C330 318 265 352 195 355 C125 358 60 330 0 318 Z" fill="var(--teal)"/>
  </svg>

  <h2 class="back__headline">Why Choose<br>Gleamworks Ovens?</h2>
  <p class="back__about">We're a local family business providing professional, non-caustic oven cleaning across Sunshine Coast. Using specialized-equipment and proven cleaning methods, equipment and proven cleaning methods, we remove heavy grease, carbon build-up, smoke residue, restoring your oven safely and effectively.</p>

  <p class="offer">Mention this flyer for<br><span class="offer__amount">$10 off</span> your first clean</p>

  <ul class="promises">
    <li>Reliable Service</li>
    <li>Non-Caustic Cleaning</li>
    <li>Satisfaction Guaranteed</li>
  </ul>

  <div class="contact-box">
    <p class="contact-box__phone">0400 528 193</p>
    <p class="contact-box__web">gleamworksovens.com.au</p>
  </div>

  <p class="extras">We also clean cooktops, rangehoods and BBQs</p>

  <div class="brand">
    <span class="brand__dot"></span>
    <span class="brand__name">Gleamworks<br>Ovens</span>
  </div>
</section>

</body>
</html>
```